Lanternfield Disability - Social Security Disability Attorneys

Our company is expanding to attract clients nationwide for our social security disability practice. We have a logo, but I am looking for a creative and elegant letterhead that projects an image of being technologically advanced but still professional enough for the legal field. I am looking for the "wow factor" combined with this is still professional enough for a law practice.

Requesting letterhead and business card design
Updates

Had to update and change the logo. The previous logo had a typo. Please send updates with the new logo for consideration. The letterhead and business cards should be professional enough to be used for a law firm. Thanks.

Industry/Entity Type

Law Practice, Law Firm, Healthcare Industry, Government

Colors

Designer to choose colors to be used in the design.

Requirements
Nice to have
• **Please create a vertical design for the business card**

```html
<!DOCTYPE html>
<html lang="en">
<head>
<meta charset="utf-8">
<title>Lanternfield Disability – Stationery</title>
<link href="https://fonts.googleapis.com/css2?family=Open+Sans:wght@400;600;700&display=swap" rel="stylesheet">
<style>
  :root{
    --stage:#2b2d31;
    --paper:#ffffff;
    --brand-blue:#0a8fe6;
    --brand-navy:#1f5fb8;
    --brand-orange:#f7860f;
    --card-orange:#f6962a;
    --ink-gray:#6b6f75;
  }
  *{box-sizing:border-box;margin:0;padding:0}
  html,body{width:1200px;height:960px;overflow:hidden;background:var(--stage);font-family:"Open Sans",Arial,sans-serif}
  .canvas{position:relative;width:1200px;height:960px}

  /* Letterhead */
  .letterhead{position:absolute;left:60px;top:50px;width:600px;height:849px;background:var(--paper);box-shadow:0 10px 30px rgba(0,0,0,.45)}
  .letterhead__accent{position:absolute;left:0;top:40px;width:50px;height:40px;background:var(--brand-blue)}
  .letterhead__name{position:absolute;left:56px;top:58px;font-size:17px;font-weight:600;color:var(--brand-navy);letter-spacing:.2px;white-space:nowrap}
  .letterhead__contact{position:absolute;left:256px;top:40px;right:0;height:40px;background:var(--brand-orange);color:#fff;font-size:7.6px;font-weight:700;padding:7px 0 0 16px;line-height:14px;white-space:nowrap}
  .letterhead__contact svg{width:8px;height:8px;vertical-align:-1px;margin-right:4px}
  .letterhead__footer{position:absolute;left:0;right:0;bottom:0;height:7px}
  .letterhead__footer svg{display:block;width:100%;height:100%}

  /* Cards */
  .card{position:absolute;width:440px;height:250px;border-radius:22px;overflow:hidden;box-shadow:0 12px 28px rgba(0,0,0,.5)}
  .card--front{left:710px;top:170px;background:var(--card-orange)}
  .card--back{left:710px;top:480px;background:var(--paper)}
  .card__name{position:absolute;left:0;right:0;top:96px;text-align:center;font-size:24px;font-weight:600;color:var(--brand-navy)}
  .card__web{position:absolute;left:0;right:0;top:150px;text-align:center;font-size:11px;color:#fff}
  .card__bands{position:absolute;inset:0}
  .card--back .card__name{left:26px;right:auto;top:100px;text-align:left;font-size:17px}
  .card__person{position:absolute;left:236px;top:78px;font-size:8px;color:#333;line-height:13px;white-space:nowrap}
  .card__person-name{font-size:13px;font-weight:600;color:var(--brand-blue);line-height:16px}
  .card__role{color:var(--ink-gray);font-size:7.5px;margin-bottom:3px}
  .card__person svg{width:7px;height:7px;vertical-align:-1px;margin-right:4px}
</style>
</head>
<body>
<div class="canvas">

  <section class="letterhead">
    <div class="letterhead__accent"></div>
    <div class="letterhead__name">Lanternfield Disability</div>
    <div class="letterhead__contact">
      <div><svg viewBox="0 0 10 10"><circle cx="5" cy="5" r="4.5" fill="none" stroke="#fff"/><circle cx="5" cy="4.5" r="1.6" fill="#fff"/></svg>00 Sample Avenue, Suite 00, California, 00000, United States</div>
      <div><svg viewBox="0 0 10 10"><circle cx="5" cy="5" r="4.5" fill="none" stroke="#fff"/><path d="M3.4 2.8l1 .9-.5.8a3 3 0 0 0 1.6 1.6l.8-.5.9 1-.8.8A4 4 0 0 1 2.6 3.6z" fill="#fff"/></svg>(000) 000-0000 &nbsp;info@lanternfielddisability.com &nbsp;www.lanternfielddisability.com</div>
    </div>
    <div class="letterhead__footer">
      <svg viewBox="0 0 600 7" preserveAspectRatio="none">
        <polygon points="0,0 176,0 172,7 0,7" fill="var(--brand-orange)"/>
        <polygon points="180,0 390,0 386,7 176,7" fill="var(--brand-blue)"/>
        <polygon points="394,0 600,0 600,7 390,7" fill="var(--brand-orange)"/>
      </svg>
    </div>
  </section>

  <section class="card card--front">
    <div class="card__name">Lanternfield Disability</div>
    <div class="card__web">www.lanternfielddisability.com</div>
  </section>

  <section class="card card--back">
    <svg class="card__bands" viewBox="0 0 440 250" preserveAspectRatio="none">
      <rect x="0" y="0" width="440" height="14" fill="var(--brand-blue)"/>
      <rect x="0" y="14" width="440" height="3" fill="var(--brand-orange)"/>
      <rect x="0" y="233" width="440" height="3" fill="var(--brand-orange)"/>
      <rect x="0" y="236" width="440" height="14" fill="var(--brand-blue)"/>
      <rect x="220" y="80" width="1.5" height="90" fill="#d5d8dc"/>
    </svg>
    <div class="card__name">Lanternfield Disability</div>
    <div class="card__person">
      <div class="card__person-name">Example Name</div>
      <div class="card__role">Designation</div>
      <div><svg viewBox="0 0 10 10"><circle cx="5" cy="5" r="5" fill="var(--brand-blue)"/><circle cx="5" cy="4.5" r="1.6" fill="#fff"/></svg>Level 00, 00 Example Street, Example 0</div>
      <div><svg viewBox="0 0 10 10"><circle cx="5" cy="5" r="5" fill="var(--brand-blue)"/></svg>0000 000 129 &nbsp;0000 000 130</div>
      <div><svg viewBox="0 0 10 10"><circle cx="5" cy="5" r="5" fill="var(--brand-blue)"/><rect x="2.5" y="3.3" width="5" height="3.4" fill="#fff"/></svg>contact@lanternfielddisability.com</div>
      <div><svg viewBox="0 0 10 10"><circle cx="5" cy="5" r="5" fill="var(--brand-blue)"/></svg>www.lanternfielddisability.com</div>
    </div>
  </section>

</div>
</body>
</html>
```